Celebration Cake brochure for boutique cake store

Looking for a cake brochure which displays the photo of the cake along with the description. Don't mind what style of brochure or size you do. We are a boutique bakery with both Italian and Australian cakes. I have a few ranges of products that I need to produce brochures (such as other sweets) but this is the first one required. *more photo to come

Industry/Entity Type

Bakery

Font styles to use
Sans Serif

Colors

Designer to choose colors to be used in the design.

Requirements
Must have
• Easy for customers to use the brochure to choose their cake. Don't mind what size brochure/menu you use

```html
<!DOCTYPE html>
<html lang="en">
<head>
<meta charset="utf-8">
<title>Celebration Cakes Brochure Spread</title>
<link rel="stylesheet" href="https://fonts.googleapis.com/css2?family=Saira+Condensed:wght@400;500;600&family=Open+Sans:wght@400;700&display=swap">
<style>
  :root {
    --backdrop: #2b2b2b;
    --sky: #a9d3ef;
    --sky-deep: #9cc8e6;
    --berry: #c6415a;
    --berry-deep: #b3283f;
    --ink: #1d1d1d;
    --paper-text: #ffffff;
    --photo-light: #8a5a34;
    --photo-dark: #2e1a0e;
  }
  * { box-sizing: border-box; margin: 0; padding: 0; }
  html, body { width: 1200px; height: 789px; overflow: hidden; }
  body {
    background: var(--backdrop);
    font-family: "Open Sans", sans-serif;
    position: relative;
  }
  .spread {
    position: absolute;
    left: 50px; top: 40px;
    width: 1100px; height: 709px;
    display: flex;
  }
  .page {
    position: relative;
    width: 550px; height: 709px;
    overflow: hidden;
  }
  .page--left { background: var(--sky); color: var(--ink); }
  .page--right { background: var(--berry); color: var(--paper-text); }
  .cake {
    position: absolute;
    width: 230px;
  }
  .cake__photo {
    width: 230px; height: 145px;
    background: radial-gradient(ellipse at 50% 55%, var(--photo-light) 0%, #5a3720 45%, var(--photo-dark) 100%);
  }
  .cake__name {
    font-family: "Saira Condensed", sans-serif;
    font-weight: 500;
    font-size: 17px;
    letter-spacing: 0.3px;
    text-transform: uppercase;
    margin-top: 6px;
    line-height: 1.1;
  }
  .cake__desc {
    font-size: 10px;
    line-height: 1.35;
    margin-top: 2px;
  }
  .col-a { left: 30px; }
  .col-b { left: 290px; }
  .row-1 { top: 30px; }
  .row-2 { top: 230px; }
  .row-3 { top: 430px; }
  .footer-band {
    position: absolute;
    left: 0; bottom: 0;
    width: 550px; height: 62px;
    display: flex; align-items: center;
    padding-left: 30px;
  }
  .page--left .footer-band { background: var(--berry-deep); color: var(--paper-text); }
  .page--right .footer-band { background: var(--sky); color: var(--berry-deep); }
  .footer-band__url {
    font-weight: 700;
    font-size: 16px;
    letter-spacing: 0.5px;
  }
  .page-number {
    position: absolute;
    bottom: 18px;
    right: 40px;
    width: 64px; height: 64px;
    border-radius: 50%;
    display: flex; align-items: center; justify-content: center;
    font-family: "Saira Condensed", sans-serif;
    font-size: 18px;
    padding-bottom: 10px;
  }
  .page--left .page-number { background: var(--sky); color: var(--ink); bottom: 10px; }
  .page--right .page-number { background: var(--berry-deep); color: var(--paper-text); bottom: 10px; }
  .gutter-shade {
    position: absolute; top: 0; bottom: 0; width: 18px;
  }
  .page--left .gutter-shade { right: 0; background: linear-gradient(to right, rgba(0,0,0,0), rgba(0,0,0,0.08)); }
  .page--right .gutter-shade { left: 0; background: linear-gradient(to left, rgba(0,0,0,0), rgba(0,0,0,0.1)); }
</style>
</head>
<body>
<main class="spread">
  <section class="page page--left">
    <article class="cake col-a row-1">
      <div class="cake__photo" role="img" aria-label="Photo of apple crumble cake on a gold board"></div>
      <h2 class="cake__name">Apple Crumble</h2>
      <p class="cake__desc">Shortbread base with diced apples, cinnamon and a crumble topping.</p>
    </article>
    <article class="cake col-a row-2">
      <div class="cake__photo" role="img" aria-label="Photo of bianco nero cake with chocolate flakes"></div>
      <h2 class="cake__name">Bianco Nero</h2>
      <p class="cake__desc">Vanilla sponge layered with fresh cream, rolled in white and dark chocolate flakes.</p>
    </article>
    <article class="cake col-a row-3">
      <div class="cake__photo" role="img" aria-label="Photo of cassata siciliana with candied fruit"></div>
      <h2 class="cake__name">Cassata Siciliana</h2>
      <p class="cake__desc">Vanilla sponge with ricotta cream, candied fruit and a pistachio marzipan coat.</p>
    </article>
    <article class="cake col-b row-1">
      <div class="cake__photo" role="img" aria-label="Photo of apple pie on a gold board"></div>
      <h2 class="cake__name">Apple Pie</h2>
      <p class="cake__desc">Baked apple in a buttery shortcrust pastry.</p>
    </article>
    <article class="cake col-b row-2">
      <div class="cake__photo" role="img" aria-label="Photo of black forest cake topped with cherries"></div>
      <h2 class="cake__name">Black Forest</h2>
      <p class="cake__desc">Chocolate sponge with cherries, fresh cream and shaved chocolate.</p>
    </article>
    <article class="cake col-b row-3">
      <div class="cake__photo" role="img" aria-label="Photo of chocolate hazelnut almond mud cake"></div>
      <h2 class="cake__name">Chocolate Hazelnut Almond Mud</h2>
      <p class="cake__desc">Rich chocolate mud with hazelnut ganache and toasted almonds.</p>
    </article>
    <footer class="footer-band"><span class="footer-band__url">www.bellavitacakes.com.au</span></footer>
    <div class="page-number">02</div>
    <div class="gutter-shade"></div>
  </section>

  <section class="page page--right">
    <article class="cake col-a row-1">
      <div class="cake__photo" role="img" aria-label="Photo of chocolate mud cake with chocolate decorations"></div>
      <h2 class="cake__name">Chocolate Mud</h2>
      <p class="cake__desc">Moist chocolate sponge with a layer of ganache, finished with chocolate.</p>
    </article>
    <article class="cake col-a row-2">
      <div class="cake__photo" role="img" aria-label="Photo of croquembouche tower with strawberries"></div>
      <h2 class="cake__name">Croquembouche</h2>
      <p class="cake__desc">Choux puffs filled with vanilla custard and bound in golden toffee.</p>
    </article>
    <article class="cake col-a row-3">
      <div class="cake__photo" role="img" aria-label="Photo of baked cheesecake with striped sugar top"></div>
      <h2 class="cake__name">Baked Cheesecake</h2>
      <p class="cake__desc">Creamy baked cheesecake on a biscuit base with almond crumb.</p>
    </article>
    <article class="cake col-b row-1">
      <div class="cake__photo" role="img" aria-label="Photo of gluten free chocolate mud cake with macarons"></div>
      <h2 class="cake__name">Gluten Free Chocolate Mud</h2>
      <p class="cake__desc">Dense gluten free chocolate cake topped with ganache and macarons.</p>
    </article>
    <article class="cake col-b row-2">
      <div class="cake__photo" role="img" aria-label="Photo of hazelnut chocolate tart"></div>
      <h2 class="cake__name">Crostata di Gianduia</h2>
      <p class="cake__desc">Shortcrust tart filled with gianduia cream and topped with toasted hazelnuts.</p>
    </article>
    <article class="cake col-b row-3">
      <div class="cake__photo" role="img" aria-label="Photo of diplomatica cake with strawberries"></div>
      <h2 class="cake__name">Diplomatica</h2>
      <p class="cake__desc">Puff pastry with vanilla custard, sponge soaked in liqueur and icing sugar.</p>
    </article>
    <footer class="footer-band"><span class="footer-band__url">www.bellavitacakes.com.au</span></footer>
    <div class="page-number">03</div>
    <div class="gutter-shade"></div>
  </section>
</main>
</body>
</html>
```